Creative Agency Showcase/Profile

Looking for a impactful, clean design to showcase our best works.

Our events company: www.brightkiteevents.com.sg

We have a clean and impactful look which we want to maintain. Looking at how we can best showcase our works/events to new customers who we want to do business with.

Actual photos will be provided once appointed.

Target Market(s)

Corporates, New Customers

Font styles to use
Sans Serif

Colors
ec1f27
0592cd
f78f20
6b439b
ffffff

Requirements
Must have
• Key Tagline:
• BREAKING NEW GROUND
• To be presented on a 16:9 Landscape format (prefably editable in KEYNOTE in the future)
• Total should be at least 8-10 pages including a COVER PAGE and CONTACT US PAGE.
Nice to have
• Some secondary captions/by lines.
• Must include event pictures.
• Hoping to have one picture per slide.
• Please use stock images at least 8-10 for now.

```html
<!DOCTYPE html>
<html lang="en">
<head>
<meta charset="utf-8">
<title>Bright Kite Events – Company Profile</title>
<link href="https://fonts.googleapis.com/css2?family=Raleway:wght@300;400;500;600;700;800&display=swap" rel="stylesheet">
<style>
:root{
  --bg:#bcdcdc;
  --paper:#ffffff;
  --paper-edge:#e9e9e9;
  --red:#ec1f27;
  --wine:#5a0c12;
  --wine-dark:#1e0406;
  --purple:#6b439b;
  --purple-deep:#2c1a4d;
  --ink:#2b2b2b;
  --muted:#777;
  --white:#ffffff;
}
*{box-sizing:border-box;margin:0;padding:0}
html,body{width:1200px;height:4093px;overflow:hidden}
body{background:var(--bg);font-family:"Raleway",sans-serif;color:var(--ink);position:relative}

.section{position:absolute;left:0;width:1200px;height:585px}
.shadow{box-shadow:0 14px 30px rgba(20,60,60,.25)}

/* cover */
.cover{position:absolute;left:220px;top:58px;width:760px;height:470px;background:var(--paper);overflow:hidden}
.cover svg{position:absolute;inset:0}
.brand{position:absolute;display:flex;align-items:center;gap:10px;color:var(--white);font-weight:700;letter-spacing:.06em;text-transform:uppercase;white-space:nowrap}
.brand .dot{width:28px;height:28px;border:2px solid currentColor;border-radius:50%;flex:none}
.cover .brand{left:48px;top:52px;font-size:20px}
.tagline{position:absolute;text-align:right;line-height:1.05;white-space:nowrap}
.tagline .light{display:block;font-weight:300}
.tagline .bold{display:block;font-weight:800}
.tagline .rule{display:inline-block;width:44px;height:4px;background:var(--red);margin-top:8px}
.cover .tagline{right:40px;top:260px;font-size:30px}

/* spreads */
.spread{position:absolute;left:100px;top:117px;width:1000px;height:350px;display:flex;background:var(--paper)}
.page{position:relative;width:500px;height:350px;overflow:hidden;background:var(--paper)}
.page + .page{border-left:1px solid var(--paper-edge)}
.page-title{position:absolute;left:28px;top:22px;font-size:15px;font-weight:500;color:var(--ink)}
.page-title::after{content:"";display:block;width:24px;height:3px;background:var(--red);margin-top:6px}

.band{position:absolute;left:0;top:64px;width:500px;height:238px;background:linear-gradient(120deg,#3a2466,#6b439b 55%,#4a2e7a)}
.band.dark{background:linear-gradient(120deg,#141020,#2c1a4d 45%,#1a1228)}
.band.mixed{background:linear-gradient(90deg,#5b3a8c,#2a1d44 55%,#161018)}
.ring{position:absolute;border:1px solid rgba(255,255,255,.35);border-radius:50%}
.shot{position:absolute;width:96px;height:96px;border-radius:50%;border:3px solid var(--white)}
.r1{top:22px}.r2{top:126px}
.c1{left:70px}.c2{left:190px}.c3{left:310px}.c4{left:130px}.c5{left:250px}

/* about spread */
.about-title{left:30px;top:70px}
.about-text{position:absolute;left:30px;top:118px;width:290px;font-size:8.5px;line-height:1.6;color:var(--muted)}
.about-text .accent{color:var(--red)}
.team-svg{position:absolute;left:0;top:0}
.team-heading{position:absolute;left:412px;top:64px;font-size:15px;color:var(--white);font-weight:400}
.team-list{position:absolute;left:405px;top:108px;list-style:none}
.team-list li{display:flex;align-items:center;gap:12px;height:50px;color:var(--white);font-size:9px;font-weight:600;letter-spacing:.06em}
.team-list .icon{width:30px;height:30px;border:1px solid rgba(255,255,255,.8);border-radius:50%;display:flex;align-items:center;justify-content:center}
.mgr-heading{position:absolute;left:536px;top:50px;font-size:15px;color:var(--white)}
.mgr-intro{position:absolute;left:700px;top:38px;width:200px;font-size:7px;line-height:1.5;color:rgba(255,255,255,.8)}
.mgr{position:absolute;display:flex;align-items:center;gap:8px;color:var(--white);font-size:7.5px;font-weight:500}
.mgr .head{width:34px;height:34px;border-radius:50%;border:2px solid var(--white);background:linear-gradient(#9a9aa5,#55556a)}

/* why us */
.why-title{position:absolute;left:28px;top:16px;font-size:14px;font-weight:500;line-height:1.25;width:320px}
.why-title::after{content:"";display:block;width:24px;height:3px;background:var(--red);margin-top:6px}
.why-brand{position:absolute;right:24px;top:22px;color:var(--red);font-size:9px;flex-direction:column;gap:3px}
.why-brand .dot{width:14px;height:14px}
.why-band{position:absolute;left:0;top:74px;width:500px;height:228px;background:linear-gradient(180deg,#3a2466 0%,#5b3a8c 45%,#1c1230 100%)}
.why-text{position:absolute;left:28px;top:92px;width:440px;font-size:7.5px;line-height:1.6;color:rgba(255,255,255,.85)}
.why-text p + p{margin-top:8px}
.why-text strong{color:var(--white)}

/* contact */
.contact-brand{left:40px;top:80px;color:var(--red);font-size:14px}
.contact-brand .dot{width:26px;height:26px}
.contact-title{position:absolute;left:40px;top:148px;font-size:17px;font-weight:700}
.contact-title::after{content:"";display:block;width:24px;height:3px;background:var(--red);margin-top:6px}
.contact-list{position:absolute;left:40px;top:190px;list-style:none;font-size:9px;line-height:1.4}
.contact-list li{display:flex;align-items:flex-start;gap:8px;margin-bottom:6px}
.contact-list svg{flex:none;margin-top:1px}
.spread .cover-mini .brand{left:36px;top:44px;font-size:12px;gap:8px}
.spread .cover-mini .brand .dot{width:20px;height:20px}
.spread .cover-mini .tagline{right:24px;top:170px;font-size:18px}
.spread .cover-mini .tagline .rule{width:30px;height:3px;margin-top:6px}
</style>
</head>
<body>

<!-- Cover -->
<section class="section" style="top:0">
  <div class="cover shadow">
    <svg width="760" height="470" viewBox="0 0 760 470">
      <defs>
        <linearGradient id="wineFill" x1="0" y1="0" x2="1" y2="1">
          <stop offset="0" stop-color="#8a1620"/>
          <stop offset=".55" stop-color="#4a0a10"/>
          <stop offset="1" stop-color="#1e0406"/>
        </linearGradient>
      </defs>
      <path d="M0 0H430C520 110 525 330 450 470H0Z" fill="var(--red)"/>
      <path d="M0 0H412C500 110 504 330 430 470H0Z" fill="url(#wineFill)" role="img" aria-label="Concert crowd with raised hands, in deep red tones"/>
    </svg>
    <div class="brand"><span class="dot"></span>Bright Kite Events</div>
    <div class="tagline"><span class="light">Breaking</span><span class="bold">New Ground</span><span class="rule"></span></div>
  </div>
</section>

<!-- About & team -->
<section class="section" style="top:585px">
  <div class="spread shadow">
    <div class="page">
      <h2 class="page-title about-title">About us</h2>
      <p class="about-text">Bright Kite Events is a Singapore events company offering the full range of high quality services, from concept and design to staging, sound and lighting. Our experienced team plans every detail so clients can relax and enjoy the day. We have worked with corporates, schools and communities on events of every size. We listen first, then build an experience your guests remember. Choose Bright Kite Events today and start your <span class="accent">unforgettable experience.</span></p>
    </div>
    <div class="page"></div>
    <svg class="team-svg" width="1000" height="350" viewBox="0 0 1000 350">
      <defs>
        <linearGradient id="purpleFill" x1="0" y1="0" x2="1" y2="1">
          <stop offset="0" stop-color="#3a2466"/>
          <stop offset=".5" stop-color="#6b439b"/>
          <stop offset="1" stop-color="#3d2670"/>
        </linearGradient>
        <clipPath id="bigCircle"><circle cx="920" cy="150" r="88"/></clipPath>
      </defs>
      <path d="M1000 0V350H430C352 300 336 130 408 55C600 22 800 8 1000 0Z" fill="#bbb"/>
      <path d="M1000 0V350H440C364 300 348 132 420 58C610 25 805 10 1000 0Z" fill="url(#purpleFill)" role="img" aria-label="Event team at work, in purple tones"/>
      <circle cx="920" cy="150" r="92" fill="#fff"/>
      <rect x="828" y="58" width="184" height="184" fill="#8a6a4a" clip-path="url(#bigCircle)" role="img" aria-label="Performer singing on a lit stage"/>
    </svg>
    <h3 class="team-heading">The Team</h3>
    <ul class="team-list">
      <li><span class="icon"><svg width="14" height="14" viewBox="0 0 14 14"><path d="M2 12L3 9L10 2L12 4L5 11Z" fill="none" stroke="#fff" stroke-width="1.2"/></svg></span>DESIGN TEAM</li>
      <li><span class="icon"><svg width="14" height="14" viewBox="0 0 14 14"><circle cx="7" cy="5" r="2.5" fill="none" stroke="#fff" stroke-width="1.2"/><path d="M2 13C2 9 12 9 12 13" fill="none" stroke="#fff" stroke-width="1.2"/></svg></span>ADMIN &amp; FINANCE</li>
      <li><span class="icon"><svg width="14" height="14" viewBox="0 0 14 14"><circle cx="7" cy="7" r="4.5" fill="none" stroke="#fff" stroke-width="1.2"/><circle cx="7" cy="7" r="1.5" fill="#fff"/></svg></span>OPERATIONS</li>
      <li><span class="icon"><svg width="14" height="14" viewBox="0 0 14 14"><path d="M3 2V12M7 2V12M11 2V12" stroke="#fff" stroke-width="1.2"/><rect x="2" y="8" width="2" height="2" fill="#fff"/><rect x="6" y="4" width="2" height="2" fill="#fff"/><rect x="10" y="7" width="2" height="2" fill="#fff"/></svg></span>AUDIO VISUAL</li>
    </ul>
    <h3 class="mgr-heading">Experience Managers</h3>
    <p class="mgr-intro">Our experience managers bring years of hands-on event work and look after every client from the first call to the final bow.</p>
    <div class="mgr" style="left:545px;top:100px"><span class="head" role="img" aria-label="Portrait of manager"></span>Joanna Tan</div>
    <div class="mgr" style="left:635px;top:88px"><span class="head" role="img" aria-label="Portrait of manager"></span>Rafael Koh</div>
    <div class="mgr" style="left:735px;top:78px"><span class="head" role="img" aria-label="Portrait of manager"></span>Adrian Lim</div>
    <div class="mgr" style="left:545px;top:160px"><span class="head" role="img" aria-label="Portrait of manager"></span>Melissa Ong</div>
    <div class="mgr" style="left:650px;top:148px"><span class="head" role="img" aria-label="Portrait of manager"></span>Priya Nair</div>
    <div class="mgr" style="left:560px;top:225px"><span class="head" role="img" aria-label="Portrait of manager"></span>Daniel Seah</div>
    <div class="mgr" style="left:670px;top:212px"><span class="head" role="img" aria-label="Portrait of manager"></span>Sarah Lee</div>
    <div class="mgr" style="left:745px;top:270px"><span class="head" role="img" aria-label="Portrait of manager"></span>Kelvin Ho</div>
  </div>
</section>

<!-- Special events / Lunch -->
<section class="section" style="top:1170px">
  <div class="spread shadow">
    <div class="page">
      <h2 class="page-title">Special Events</h2>
      <div class="band" role="img" aria-label="Crowd at a special event, in purple tones">
        <span class="ring" style="left:-40px;top:120px;width:140px;height:140px"></span>
        <span class="ring" style="left:400px;top:60px;width:160px;height:160px"></span>
        <span class="shot r1 c1" style="background:#6f8a5a" role="img" aria-label="Outdoor team event on a field"></span>
        <span class="shot r1 c2" style="background:#b04040" role="img" aria-label="Guests posing at a festive event"></span>
        <span class="shot r1 c3" style="background:#8a3a3a" role="img" aria-label="Performer waving a flag"></span>
        <span class="shot r2 c4" style="background:#9a7a6a" role="img" aria-label="Guests at a craft activity"></span>
        <span class="shot r2 c5" style="background:#7a5a4a" role="img" aria-label="Singer performing on stage"></span>
      </div>
    </div>
    <div class="page">
      <h2 class="page-title">Lunch &amp; Activations</h2>
      <div class="band" role="img" aria-label="Activation event crowd, in purple tones">
        <span class="ring" style="left:-50px;top:-40px;width:160px;height:160px"></span>
        <span class="ring" style="left:420px;top:130px;width:150px;height:150px"></span>
        <span class="shot r1 c1" style="background:#7a2a3a" role="img" aria-label="Band playing at a lunch event"></span>
        <span class="shot r1 c2" style="background:#8c8c98" role="img" aria-label="Guests at a product launch"></span>
        <span class="shot r1 c3" style="background:#9a7a3a" role="img" aria-label="Brand activation booth"></span>
        <span class="shot r2 c4" style="background:#5a8a6a" role="img" aria-label="Performers in colourful costumes"></span>
        <span class="shot r2 c5" style="background:#6a7a4a" role="img" aria-label="Guests at a mall activation"></span>
      </div>
    </div>
  </div>
</section>

<!-- Family day / Awards -->
<section class="section" style="top:1755px">
  <div class="spread shadow">
    <div class="page">
      <h2 class="page-title">Family Day &amp; Carnivals</h2>
      <div class="band" role="img" aria-label="Family day crowd, in purple tones">
        <span class="ring" style="left:-40px;top:110px;width:150px;height:150px"></span>
        <span class="ring" style="left:410px;top:140px;width:150px;height:150px"></span>
        <span class="shot r1 c1" style="background:#b04848" role="img" aria-label="Family in matching red shirts"></span>
        <span class="shot r1 c2" style="background:#a07050" role="img" aria-label="Children at a carnival game"></span>
        <span class="shot r1 c3" style="background:#4a6a4a" role="img" aria-label="Host on stage at a carnival"></span>
        <span class="shot r2 c4" style="background:#c09a60" role="img" aria-label="Costumed performer at a celebration"></span>
        <span class="shot r2 c5" style="background:#6a8aa0" role="img" aria-label="Guests at an outdoor carnival"></span>
      </div>
    </div>
    <div class="page">
      <h2 class="page-title">Award ceremonies</h2>
      <div class="band dark" role="img" aria-label="Award ceremony hall, in dark tones">
        <span class="ring" style="left:380px;top:-30px;width:170px;height:170px"></span>
        <span class="shot r1 c1" style="background:#8a9a30" role="img" aria-label="Laser light show on stage"></span>
        <span class="shot r1 c2" style="background:#4a4a7a" role="img" aria-label="Presenter on a lit stage"></span>
        <span class="shot r1 c3" style="background:#6a6a80" role="img" aria-label="Winners posing with awards"></span>
        <span class="shot r2 c4" style="background:#4a7a5a" role="img" aria-label="Stage with green lighting"></span>
        <span class="shot r2 c5" style="background:#b06a3a" role="img" aria-label="Musician performing at a ceremony"></span>
      </div>
    </div>
  </div>
</section>

<!-- Dinner & dance / Why us -->
<section class="section" style="top:2340px">
  <div class="spread shadow">
    <div class="page">
      <h2 class="page-title">Dinner &amp; Dance</h2>
      <div class="band mixed" role="img" aria-label="Dinner and dance hall, in purple tones">
        <span class="ring" style="left:-40px;top:100px;width:150px;height:150px"></span>
        <span class="shot r1 c1" style="background:#5a6aa0" role="img" aria-label="Dancer in costume on stage"></span>
        <span class="shot r1 c2" style="background:#8a6a5a" role="img" aria-label="Guests in formal wear"></span>
        <span class="shot r1 c3" style="background:#c07060" role="img" aria-label="Guests in festive costumes"></span>
        <span class="shot r2 c4" style="background:#4a5a8a" role="img" aria-label="Band on a dinner stage"></span>
        <span class="shot r2 c5" style="background:#8a8a6a" role="img" aria-label="Guests in themed outfits"></span>
      </div>
    </div>
    <div class="page">
      <h2 class="why-title">What Makes us the Best Event Company in Singapore?</h2>
      <div class="brand why-brand"><span class="dot"></span>Bright Kite Events</div>
      <div class="why-band" role="img" aria-label="Concert crowd silhouettes, in purple tones"></div>
      <div class="why-text">
        <p>We are a full service event company creating team building, corporate events and special events in a professional manner to ensure everyone has an enjoyable outing. <strong>We look forward to serving you!</strong></p>
        <p>From dinner and dance to award ceremonies and family carnivals, our crew and in-house audio visual gear deliver smooth shows across Singapore.</p>
      </div>
    </div>
  </div>
</section>

<!-- Back & front cover -->
<section class="section" style="top:2925px">
  <div class="spread shadow">
    <div class="page">
      <svg width="500" height="350" viewBox="0 0 500 350" style="position:absolute;inset:0">
        <defs>
          <linearGradient id="wineFill2" x1="0" y1="0" x2="1" y2="1">
            <stop offset="0" stop-color="#8a1620"/>
            <stop offset="1" stop-color="#1e0406"/>
          </linearGradient>
        </defs>
        <path d="M500 0V350H300C230 270 220 90 290 0Z" fill="var(--red)"/>
        <path d="M500 0V350H312C244 270 234 90 304 0Z" fill="url(#wineFill2)" role="img" aria-label="Concert crowd, in deep red tones"/>
      </svg>
      <div class="brand contact-brand"><span class="dot"></span>Bright Kite Events</div>
      <h2 class="contact-title">Contact us</h2>
      <ul class="contact-list">
        <li><svg width="10" height="10" viewBox="0 0 10 10"><path d="M2 1L4 3L3 4.5C4 6 5 7 5.5 7L7 6L9 8L8 9C5 9 1 5 1 2Z" fill="var(--red)"/></svg>+65 6100 2345</li>
        <li><svg width="10" height="10" viewBox="0 0 10 10"><path d="M2 1L4 3L3 4.5C4 6 5 7 5.5 7L7 6L9 8L8 9C5 9 1 5 1 2Z" fill="var(--red)"/></svg>+65 6100 6789</li>
        <li><svg width="10" height="10" viewBox="0 0 10 10"><rect x="1" y="2" width="8" height="6" fill="var(--red)"/><path d="M1 2L5 5.5L9 2" stroke="#fff" fill="none"/></svg>hello@brightkiteevents.com.sg</li>
        <li><svg width="10" height="10" viewBox="0 0 10 10"><path d="M5 9C5 9 1.5 5.5 1.5 3.5A3.5 3.5 0 0 1 8.5 3.5C8.5 5.5 5 9 5 9Z" fill="var(--red)"/><circle cx="5" cy="3.5" r="1.2" fill="#fff"/></svg>18 Harbour Link #03-07,<br>Singapore 539876</li>
        <li><svg width="10" height="10" viewBox="0 0 10 10"><circle cx="5" cy="5" r="4" fill="none" stroke="var(--red)"/><path d="M1 5H9M5 1C3 3 3 7 5 9M5 1C7 3 7 7 5 9" stroke="var(--red)" fill="none" stroke-width=".8"/></svg>www.brightkiteevents.com.sg</li>
      </ul>
    </div>
    <div class="page cover-mini">
      <svg width="500" height="350" viewBox="0 0 500 350" style="position:absolute;inset:0">
        <path d="M0 0H272C336 80 340 250 290 350H0Z" fill="var(--red)"/>
        <path d="M0 0H258C322 80 326 250 276 350H0Z" fill="url(#wineFill2)" role="img" aria-label="Concert crowd with raised hands, in deep red tones"/>
      </svg>
      <div class="brand"><span class="dot"></span>Bright Kite Events</div>
      <div class="tagline"><span class="light">Breaking</span><span class="bold">New Ground</span><span class="rule"></span></div>
    </div>
  </div>
</section>

</body>
</html>
```